Personal Business Card

I am an award winning banjo player who plays with two different professional bands. My experiences include studio recordings for other artists and played the theme song for the Creature Channel's "Frontier Tundra Trails". I am ready to take my career to the next level and would like something that will look professional. it is important to me to have a banjo on the card. If possible my accomplishments to be put on back of card.

Industry/Entity Type

Artists

Contact Information for Business Card

Corbin Halloway
cell 602-315-2860
email corbinhallowaybanjo@mailvista.net

2008 AZ Banjo Champion
2008 Pinebrook Banjo Champion
2010 AZ Banjo Champion
2010 Riverbend Hoedown Talcott Banjo Champion
2010 Cedar Hollow Gathering Banjo Finalist

```html
<!DOCTYPE html>
<html lang="en">
<head>
<meta charset="utf-8">
<title>Corbin Halloway – Banjo Artist Business Card</title>
<link href="https://fonts.googleapis.com/css2?family=Tinos:wght@400;700&display=swap" rel="stylesheet">
<style>
  :root {
    --backdrop: #ebe7e3;
    --tan: #b98d72;
    --card-white: #ffffff;
    --ink: #141414;
    --staff: #3a3a3a;
  }
  html, body {
    margin: 0;
    padding: 0;
    width: 1200px;
    height: 707px;
    overflow: hidden;
    background: var(--backdrop);
  }
  .sheet {
    position: relative;
    width: 1200px;
    height: 707px;
    display: flex;
    align-items: center;
    justify-content: center;
    gap: 40px;
  }
  .card {
    width: 540px;
    height: 309px;
    box-shadow: 0 6px 18px rgba(0,0,0,0.18);
    display: block;
  }
  .card text {
    font-family: 'Tinos', 'Times New Roman', serif;
    fill: var(--ink);
  }
  .tan-fill { fill: var(--tan); }
  .white-fill { fill: var(--card-white); }
  .curve-edge { fill: none; stroke: var(--ink); stroke-width: 3.5; stroke-linecap: round; }
  .staff-line { stroke: var(--staff); stroke-width: 1; }
  .note-row { fill: var(--ink); opacity: 0.10; }
  .banjo-art { fill: var(--ink); }
  .name { font-size: 31px; }
  .role { font-size: 15px; }
  .credit { font-size: 11px; }
  .back-name { font-size: 24px; }
  .back-role { font-size: 12px; }
  .contact { font-size: 14px; }
  .award { font-size: 11.5px; }
</style>
</head>
<body>
<main class="sheet">

  <svg class="card card-front" viewBox="0 0 540 309" xmlns="http://www.w3.org/2000/svg">
    <rect class="white-fill" x="0" y="0" width="540" height="309"/>
    <path class="tan-fill" d="M0 0 H540 V14 C525 90 450 110 370 118 C300 122 240 126 190 140 C175 146 165 158 160 170 C130 200 80 222 0 228 Z"/>
    <path class="curve-edge" d="M540 14 C525 90 450 110 370 118 C300 122 240 126 190 140 C175 146 165 158 160 170 C130 200 80 222 0 228"/>

    <rect class="banjo-art" role="img" aria-label="Banjo illustration" x="252" y="22" width="42" height="110" rx="20"/>

    <text class="name" x="360" y="162" text-anchor="middle">Corbin Halloway</text>
    <text class="role" x="360" y="184" text-anchor="middle">Banjo Artist</text>
    <text class="credit" x="528" y="210" text-anchor="end">Played the theme song for the Creature Channel's "Frontier Tundra Trails"</text>

    <g class="staff">
      <line class="staff-line" x1="12" y1="246" x2="528" y2="246"/>
      <line class="staff-line" x1="12" y1="252" x2="528" y2="252"/>
      <line class="staff-line" x1="12" y1="258" x2="528" y2="258"/>
      <line class="staff-line" x1="12" y1="264" x2="528" y2="264"/>
      <line class="staff-line" x1="12" y1="270" x2="528" y2="270"/>
    </g>
    <rect class="note-row" role="img" aria-label="Row of musical notes on the staff" x="16" y="234" width="508" height="42"/>
  </svg>

  <svg class="card card-back" viewBox="0 0 540 309" xmlns="http://www.w3.org/2000/svg">
    <rect class="tan-fill" x="0" y="0" width="540" height="309"/>

    <text class="back-name" x="22" y="40">Corbin Halloway</text>
    <text class="back-role" x="52" y="58">Banjo Artist</text>

    <text class="contact" x="518" y="84" text-anchor="end">Cell: 602-315-2860</text>
    <text class="contact" x="518" y="104" text-anchor="end">Email: corbinhallowaybanjo@mailvista.net</text>

    <g class="staff">
      <line class="staff-line" x1="12" y1="128" x2="528" y2="128"/>
      <line class="staff-line" x1="12" y1="134" x2="528" y2="134"/>
      <line class="staff-line" x1="12" y1="140" x2="528" y2="140"/>
      <line class="staff-line" x1="12" y1="146" x2="528" y2="146"/>
      <line class="staff-line" x1="12" y1="152" x2="528" y2="152"/>
    </g>
    <rect class="note-row" role="img" aria-label="Row of musical notes on the staff" x="16" y="116" width="508" height="42"/>

    <g class="awards">
      <text class="award" x="22" y="184">2008 AZ Banjo Champion</text>
      <text class="award" x="22" y="202">2008 Pinebrook Banjo Champion</text>
      <text class="award" x="22" y="220">2010 AZ Banjo Champion</text>
      <text class="award" x="22" y="238">2010 Riverbend Hoedown Talcott Banjo Champion</text>
      <text class="award" x="22" y="256">2010 Cedar Hollow Gathering Banjo Finalist</text>
    </g>
  </svg>

</main>
</body>
</html>
```